2021 Beatwalker's Statute Compendium

Each year I public a law book for Massachusetts Police Officers, along with an accompanying motor vehicle cruiser guide. They have the same/similar design but the motor vehicle guide has a motor vehicle twist to it. The main book with be full-size with a front, back and spine. The accompanying cruiser guide will be smaller 5X7 with a spiral binding.
The year should be somewhat prominent so people know it is a new year edition. I attached some previous versions and commonly used logos.

Target Market(s)

Police Departments, Police Officers

Requirements
Must have
• Accompanying motor vehicle cruiser guide design, can be the same with a slight modification to gear it toward motor vehicle laws/rules.

The year of publishing - 2021
Nice to have
• Real images
Should not have
• Foreign (non-US) images of police.

```html
<!DOCTYPE html>
<html lang="en">
<head>
<meta charset="utf-8">
<title>2021 Beatwalker's Statute Compendium</title>
<link rel="stylesheet" href="https://fonts.googleapis.com/css2?family=Saira+Condensed:wght@500;600;700&display=swap">
<style>
  :root {
    --navy: #0c1226;
    --navy-deep: #080d1c;
    --gold: #f9c52a;
    --gold-text: #f5c518;
    --white: #ffffff;
    --bar: #0a0f1f;
  }
  * { margin: 0; padding: 0; box-sizing: border-box; }
  html, body { width: 857px; height: 1200px; overflow: hidden; background: var(--navy); }
  .cover {
    position: relative; width: 857px; height: 1200px; overflow: hidden;
    background: linear-gradient(180deg, #1b3d78 0%, #142a55 9%, var(--navy) 24%, var(--navy-deep) 100%);
    font-family: "Saira Condensed", "Arial Narrow", sans-serif;
    color: var(--white);
  }
  .top-texture {
    position: absolute; left: 0; top: 0; width: 857px; height: 230px;
    background: radial-gradient(ellipse at 50% 0%, rgba(160,60,110,.45) 0%, rgba(40,90,170,.35) 45%, rgba(12,18,38,0) 80%);
  }
  .author-arc { position: absolute; left: 62px; top: 62px; width: 772px; height: 46px; }
  .author-name {
    position: absolute; left: 62px; top: 70px; width: 772px; text-align: center;
    font-weight: 700; font-size: 31px; line-height: 36px; color: var(--bar);
  }
  .office-bar {
    position: absolute; left: 62px; top: 107px; width: 771px; height: 43px;
    background: var(--bar); text-align: center;
    font-weight: 600; font-size: 22px; line-height: 43px; letter-spacing: .2px;
  }
  .photo { position: absolute; }
  .photo-lightbar { left: 62px; top: 150px; width: 771px; height: 263px;
    background: linear-gradient(100deg, #8a0f18 0%, #d8242e 30%, #b21c2a 52%, #7d8fb0 70%, #2f4f9a 88%, #e8e8ec 100%); }
  .photo-officer { left: 62px; top: 413px; width: 483px; height: 334px;
    background: linear-gradient(120deg, #0d3e8c 0%, #1b4f9e 40%, #101f3e 75%, #0b1630 100%); }
  .photo-arrest { left: 545px; top: 413px; width: 288px; height: 334px;
    background: linear-gradient(160deg, #3e3f44 0%, #4b4c52 40%, #3d5a7c 70%, #6fa07a 100%); }
  .seal { position: absolute; left: 660px; top: 706px; width: 72px; height: 94px; }
  .brand {
    position: absolute; left: 347px; top: 790px; width: 206px; text-align: center;
  }
  .brand-dot { display: block; width: 92px; height: 92px; margin: 0 auto 12px; border-radius: 50%; background: var(--gold); }
  .brand-name { font-weight: 700; font-size: 30px; line-height: 34px; color: var(--gold-text); }
  .title-block { position: absolute; left: 64px; top: 795px; width: 290px; }
  .title-kicker { font-weight: 600; font-size: 36px; line-height: 40px; color: var(--gold-text); }
  .title-main { position: relative; margin-top: 6px; }
  .title-word { font-weight: 600; font-size: 62px; line-height: 58px; }
  .title-sub { font-weight: 600; font-size: 34px; line-height: 38px; }
  .title-year {
    position: absolute; left: 212px; top: -2px; font-weight: 600;
    font-size: 58px; line-height: 50px; text-align: left;
  }
  .guide { position: absolute; left: 560px; top: 810px; width: 268px; text-align: center; }
  .guide-state { font-weight: 700; font-size: 32px; line-height: 36px; color: var(--gold-text); }
  .guide-kicker { font-weight: 600; font-size: 20px; line-height: 24px; color: var(--gold-text); }
  .guide-topics { font-weight: 600; font-size: 20px; line-height: 23px; }
  .rights {
    position: absolute; left: 0; top: 1138px; width: 857px; text-align: center;
    font-weight: 600; font-size: 20px; line-height: 24px;
  }
</style>
</head>
<body>
<main class="cover">
  <div class="top-texture" role="img" aria-label="Hexagon pattern backdrop in blue and magenta"></div>

  <svg class="author-arc" viewBox="0 0 772 46" aria-hidden="true">
    <path d="M0 46 Q386 -14 772 46 Z" fill="#f9c52a"/>
  </svg>
  <h2 class="author-name">ATTORNEY DORIAN K. WHITFIELD</h2>
  <div class="office-bar">THE LAW OFFICE OF DORIAN K. WHITFIELD</div>

  <div class="photo photo-lightbar" role="img" aria-label="Close-up photo of a red and blue police cruiser light bar"></div>
  <div class="photo photo-officer" role="img" aria-label="Photo of a police officer aiming a handgun in a transit station"></div>
  <div class="photo photo-arrest" role="img" aria-label="Photo of a suspect's hands in handcuffs behind his back"></div>

  <svg class="seal" viewBox="0 0 72 94" aria-hidden="true">
    <circle cx="36" cy="52" r="34" fill="#c9982a"/>
  </svg>

  <div class="brand">
    <span class="brand-dot" aria-hidden="true"></span>
    <div class="brand-name">WHITFIELD TRAINING</div>
  </div>

  <h1 class="title-block">
    <div class="title-kicker">BEATWALKER´S</div>
    <div class="title-main">
      <div class="title-word">STATUTE</div>
      <div class="title-sub">COMPENDIUM</div>
      <div class="title-year">20<br>21</div>
    </div>
  </h1>

  <section class="guide">
    <div class="guide-state">MASSACHUSSETTS</div>
    <div class="guide-kicker">POLICE OFFICER´S GUIDE TO:</div>
    <div class="guide-topics">CRIMINAL PROCEDURE,<br>STATUTORY LAW,<br>MOTORVEHICLE LAW<br>AND JUVENILE LAW.</div>
  </section>

  <footer class="rights">© WHITFIELD CONSULTING, LLC. ALL RIGHTS RESERVED</footer>
</main>
</body>
</html>
```